Jotle - sticky notes for DeskOS landing page single page html + css

Is landing page for a new DeskOS app, I need just one single page explaing some features.

I will attach some materials to get insiprations.

Should be used the latest model of devices and some nice features
you can try the app here http://qv.example/f/K8R2

Jotle is a simple note taking app for DeskOS

Features:
- SkyVault Sync on differnt Deskbook
- Private notes
- PressKey Support on Deskbook to quick unlock
- Custom Colors
- Rich Text editing
- Glide Strip support
- Autolock private notes after user activity

some text should be present as spot
Updates

We have a new icon: http://qv.example/i/pm47

Project Deadline Extended
Reason: Delayed to have more time to develope ideas

Target Market(s)

US

Industry/Entity Type

Software

Coding

Coded - Design and coding required

Number of Pages Required

1 page

Font styles to use
Sans Serif

Colors
fbed22

Requirements
Must have
• Fast load and adaptable to verious devices
• some menu that point down to the features sections
• - link to Desk App Depot with badge
• - Form to subscribe a newsletter
• - Use some claim text
• - Avenir font
• some screenshot of the prduct
Nice to have
• some animations but not to much
• references:
• http://quillhourapp.example
• https://marovinapp.example
• http://www.hueforge.example/mac/
• https://crankworks.example/clipmule/
• https://crankworks.example/chirpling/mac/
• http://www.otter-scribe.example
Should not have
• slow load

```html
<!DOCTYPE html>
<html lang="en">
<head>
<meta charset="utf-8">
<title>Jotle – sticky notes for DeskOS</title>
<link rel="stylesheet" href="https://fonts.googleapis.com/css2?family=Nunito+Sans:wght@300;400;600;700;800&family=Open+Sans:wght@400;600&family=Oswald:wght@500&display=swap">
<style>
  :root{
    --yellow:#fbed22;
    --yellow-deep:#fdd000;
    --ink:#1f1f1f;
    --text:#444;
    --muted:#777;
    --hero-dark:#241d1a;
    --hero-mid:#4a3b31;
    --footer:#2d2d2d;
    --white:#fff;
    --rule:#e6d66a;
  }
  *{margin:0;padding:0;box-sizing:border-box}
  html,body{width:1200px;height:2941px;overflow:hidden}
  body{position:relative;background:var(--white);font-family:"Open Sans",sans-serif;color:var(--text)}
  .abs{position:absolute}

  /* Hero */
  .hero{left:0;top:0;width:1200px;height:624px;background:radial-gradient(ellipse at 50% 55%,var(--hero-mid),var(--hero-dark) 75%)}
  .nav a{position:absolute;top:86px;color:var(--white);font:700 13px "Nunito Sans",sans-serif;text-decoration:none;letter-spacing:.3px}
  .brand{position:absolute;left:524px;top:62px;width:152px;height:62px;display:flex;align-items:center;justify-content:center;font:700 34px "Nunito Sans",sans-serif;color:var(--yellow)}
  .btn-login{position:absolute;left:945px;top:80px;width:71px;height:27px;border:1px solid var(--white);border-radius:3px;color:var(--white);font:700 11px "Nunito Sans",sans-serif;display:flex;align-items:center;justify-content:center}
  .btn-signup{position:absolute;left:1027px;top:80px;width:71px;height:27px;background:var(--yellow-deep);border-radius:3px;color:var(--ink);font:700 11px "Nunito Sans",sans-serif;display:flex;align-items:center;justify-content:center}
  .hero-title{left:0;top:208px;width:1200px;text-align:center;color:var(--white);font:800 42px "Nunito Sans",sans-serif}
  .hero-sub{left:300px;top:262px;width:600px;text-align:center;color:#eee;font-size:13px;line-height:22px}
  .arrow{top:303px}
  .devices{left:235px;top:349px;width:785px;height:376px;border-radius:14px;background:linear-gradient(135deg,#3a3a3a 0%,#d9d9d9 45%,#f2f2f2 60%,#fbe34a 100%)}

  /* Welcome */
  .welcome-title{left:0;top:808px;width:1200px;text-align:center;font:600 40px "Nunito Sans",sans-serif;color:var(--ink)}
  .divider{left:480px;top:870px}
  .welcome-text{left:160px;top:902px;width:880px;text-align:center;font-size:11.5px;line-height:20px;color:#555}
  .platform-icon{width:94px;height:94px;border-radius:50%;background:var(--yellow-deep);display:flex;align-items:center;justify-content:center;top:1030px}
  .platform-name{top:1026px;font:400 21px "Nunito Sans",sans-serif;color:#555}
  .platform-text{top:1062px;width:190px;font-size:11px;line-height:20px;color:var(--muted)}

  /* Features */
  .features{left:0;top:1225px;width:1200px;height:492px;background:linear-gradient(180deg,var(--yellow-deep),#ffe21a 50%,var(--yellow-deep))}
  .features-art{left:157px;top:1300px;width:411px;height:333px;border-radius:14px;background:linear-gradient(160deg,#fff3a8,#f6d400 70%)}
  .features-title{left:641px;top:1328px;font:800 38px "Nunito Sans",sans-serif;color:var(--ink)}
  .features-intro{left:641px;top:1392px;width:420px;font:700 12px "Nunito Sans",sans-serif;line-height:22px;color:var(--ink)}
  .feature-list{left:641px;top:1464px;list-style:none}
  .feature-list li{display:flex;align-items:center;gap:12px;height:24.3px;font:700 13px "Nunito Sans",sans-serif;color:var(--ink)}

  /* Store */
  .store-title{left:100px;top:1822px;font:600 31px "Nunito Sans",sans-serif;color:var(--ink)}
  .store-sub{left:100px;top:1865px;font:400 17px "Nunito Sans",sans-serif;color:#333}
  .store-text{left:100px;top:1902px;width:525px;font-size:11px;line-height:21px;color:#666}
  .badge{top:2023px;height:43px;border-radius:6px;background:#111;border:1px solid #888}
  .store-shot{left:672px;top:1797px;width:528px;height:340px;border-radius:24px 0 0 24px;background:linear-gradient(135deg,#e6e6e6,#5c9b3a 40%,#2f6a1e 70%,#f3ef9a)}

  /* Newsletter */
  .newsletter{left:0;top:2209px;width:1200px;height:396px;background:linear-gradient(180deg,#fff000,var(--yellow-deep))}
  .newsletter-phone{left:314px;top:2248px;width:152px;height:310px;border-radius:28px;background:linear-gradient(180deg,#f2f2f2,#ffd800 30%,#ffd800 80%,#ececec)}
  .newsletter-title{left:517px;top:2292px;font:500 35px "Oswald",sans-serif;color:#2b2b2b;letter-spacing:.5px}
  .newsletter-text{left:517px;top:2347px;width:420px;font-size:11px;line-height:20px;color:#333}
  .email-field{left:517px;top:2393px;width:415px;height:44px;background:var(--white);border:1px solid #ddd;display:flex;align-items:center;gap:10px;padding-left:16px;font-size:11px;color:#aaa}
  .signup-btn{left:517px;top:2460px;width:131px;height:36px;background:#222;color:var(--white);font:500 13px "Oswald",sans-serif;display:flex;align-items:center;justify-content:center}

  /* Disclaimer */
  .disclaimer-title{left:182px;top:2663px;font:700 25px "Nunito Sans",sans-serif;color:var(--ink)}
  .disclaimer-text{left:368px;top:2640px;width:660px;font-size:11px;line-height:21px;color:#444}

  /* Footer */
  .footer{left:0;top:2750px;width:1200px;height:191px;background:var(--footer)}
  .social{top:2807px;width:28px;height:28px;border-radius:50%;background:var(--white)}
  .footer-links{left:0;top:2852px;width:1200px;text-align:center;font-size:11px;color:var(--white);letter-spacing:.4px}
  .footer-copy{left:0;top:2878px;width:1200px;text-align:center;font-size:12px;color:var(--white)}
</style>
</head>
<body>

<header class="abs hero">
  <nav class="nav">
    <a style="left:98px">HOME</a>
    <a style="left:180px">ABOUT</a>
    <a style="left:267px">HOW IT WORK</a>
    <a style="left:400px">FEATURES</a>
    <div class="brand">Jotle</div>
    <a style="left:731px">PRICING</a>
    <a style="left:823px">CONTACT US</a>
    <div class="btn-login">LOG IN</div>
    <div class="btn-signup">SIGN UP</div>
  </nav>
  <h1 class="abs hero-title">DESK APP DEPOT</h1>
  <p class="abs hero-sub">Sed ut perspiciatis unde omnis iste natus error sit voluptatem accusantium doloremque laudantium, totam rem aperiam, eaque ipsa quae ab illo inventore veritatis et quasi</p>
  <svg class="abs arrow" style="left:36px" width="30" height="60" viewBox="0 0 30 60"><polyline points="26,2 4,30 26,58" fill="none" stroke="#ccc" stroke-width="2"/></svg>
  <svg class="abs arrow" style="left:1134px" width="30" height="60" viewBox="0 0 30 60"><polyline points="4,2 26,30 4,58" fill="none" stroke="#ccc" stroke-width="2"/></svg>
</header>
<div class="abs devices" role="img" aria-label="Jotle running on a laptop, tablet and phone"></div>

<section class="welcome">
  <h2 class="abs welcome-title">Welcome To Jotle</h2>
  <svg class="abs divider" width="240" height="14" viewBox="0 0 240 14">
    <line x1="0" y1="7" x2="108" y2="7" stroke="var(--rule)" stroke-width="1"/>
    <line x1="132" y1="7" x2="240" y2="7" stroke="var(--rule)" stroke-width="1"/>
    <circle cx="120" cy="7" r="6" fill="none" stroke="#c9a800" stroke-width="1.5"/>
    <circle cx="120" cy="7" r="2.5" fill="#c9a800"/>
  </svg>
  <p class="abs welcome-text">Lorem ipsum dolor sit amet, consectetur adipiscing elit, sed do eiusmod tempor incididunt ut labore et dolore magna aliqua. Ut enim ad minim veniam, quis nostrud exercitation ullamco laboris nisi ut aliquip ex ea commodo consequat. Duis aute irure dolor in reprehenderit in voluptate velit esse cillum dolore eu fugiat nulla pariatur. Excepteur sint occaecat cupidatat non proident, sunt in culpa qui officia deserunt mollit anim id est laborum</p>

  <div class="abs platform-icon" style="left:98px"><svg width="34" height="44" viewBox="0 0 34 44"><rect x="2" y="2" width="30" height="40" rx="5" fill="none" stroke="#222" stroke-width="3"/><circle cx="17" cy="36" r="2" fill="#222"/></svg></div>
  <h3 class="abs platform-name" style="left:214px">Orbit OS Apps</h3>
  <p class="abs platform-text" style="left:214px">Lorem ipsum dolor sit amet, coetur adipiscing elit. Vivamus luctus urna sed urna ultricies ac tempor</p>

  <div class="abs platform-icon" style="left:451px"><svg width="34" height="44" viewBox="0 0 34 44"><rect x="2" y="2" width="30" height="40" rx="5" fill="none" stroke="#222" stroke-width="3"/><circle cx="17" cy="36" r="2" fill="#222"/></svg></div>
  <h3 class="abs platform-name" style="left:564px">Sprocket Apps</h3>
  <p class="abs platform-text" style="left:564px">Lorem ipsum dolor sit amet, coetur adipiscing elit. Vivamus luctus urna sed urna ultricies ac tempor</p>

  <div class="abs platform-icon" style="left:803px"><svg width="34" height="44" viewBox="0 0 34 44"><rect x="2" y="2" width="30" height="40" rx="5" fill="none" stroke="#222" stroke-width="3"/><circle cx="17" cy="36" r="2" fill="#222"/></svg></div>
  <h3 class="abs platform-name" style="left:917px">Pane Mobile</h3>
  <p class="abs platform-text" style="left:917px">Lorem ipsum dolor sit amet, coetur adipiscing elit. Vivamus luctus urna sed urna ultricies ac tempor</p>
</section>

<section class="abs features" id="features"></section>
<div class="abs features-art" role="img" aria-label="Jotle cloud syncing notes to a phone, tablet and laptop"></div>
<h2 class="abs features-title">Our Features</h2>
<p class="abs features-intro">Sed ut perspiciatis unde omnis iste natus error sit voluptatem accusantium doloremque laudantium, totam rem aperiam, eaque ipsa quae ab illo inventore veritatis et quasi architecto beatae vitae dicta</p>
<ul class="abs feature-list">
  <li><svg width="13" height="13" viewBox="0 0 13 13"><circle cx="6.5" cy="6.5" r="6.5" fill="#111"/><polyline points="5,3.5 8,6.5 5,9.5" fill="none" stroke="#ffe000" stroke-width="1.6"/></svg>SkyVault Sync on differnt Deskbook</li>
  <li><svg width="13" height="13" viewBox="0 0 13 13"><circle cx="6.5" cy="6.5" r="6.5" fill="#111"/><polyline points="5,3.5 8,6.5 5,9.5" fill="none" stroke="#ffe000" stroke-width="1.6"/></svg>Private notes</li>
  <li><svg width="13" height="13" viewBox="0 0 13 13"><circle cx="6.5" cy="6.5" r="6.5" fill="#111"/><polyline points="5,3.5 8,6.5 5,9.5" fill="none" stroke="#ffe000" stroke-width="1.6"/></svg>PressKey Support on Deskbook to quick unlock</li>
  <li><svg width="13" height="13" viewBox="0 0 13 13"><circle cx="6.5" cy="6.5" r="6.5" fill="#111"/><polyline points="5,3.5 8,6.5 5,9.5" fill="none" stroke="#ffe000" stroke-width="1.6"/></svg>Custom Colors</li>
  <li><svg width="13" height="13" viewBox="0 0 13 13"><circle cx="6.5" cy="6.5" r="6.5" fill="#111"/><polyline points="5,3.5 8,6.5 5,9.5" fill="none" stroke="#ffe000" stroke-width="1.6"/></svg>Rich Text editing</li>
  <li><svg width="13" height="13" viewBox="0 0 13 13"><circle cx="6.5" cy="6.5" r="6.5" fill="#111"/><polyline points="5,3.5 8,6.5 5,9.5" fill="none" stroke="#ffe000" stroke-width="1.6"/></svg>Glide Strip support</li>
  <li><svg width="13" height="13" viewBox="0 0 13 13"><circle cx="6.5" cy="6.5" r="6.5" fill="#111"/><polyline points="5,3.5 8,6.5 5,9.5" fill="none" stroke="#ffe000" stroke-width="1.6"/></svg>Autolock private notes after user activity</li>
</ul>

<section class="store">
  <h2 class="abs store-title">DESK APP DEPOT</h2>
  <p class="abs store-sub">Duis aute irure dolor in reprehenderit</p>
  <p class="abs store-text">Nemo enim ipsam voluptatem quia voluptas sit aspernatur aut odit aut fugit, sed quia consequuntur magni dolores eos qui ratione voluptatem sequi nesciunt. Neque porro quisquam est, qui dolorem ipsum quia dolor sit amet, consectetur, adipisci velit, sed quia non numquam eius modi tempora incidunt ut labore</p>
  <div class="abs badge" style="left:100px;width:149px"></div>
  <div class="abs badge" style="left:261px;width:151px"></div>
  <div class="abs store-shot" role="img" aria-label="Tablet screenshot of Jotle notes over a green desktop"></div>
</section>

<section class="abs newsletter"></section>
<div class="abs newsletter-phone" role="img" aria-label="Phone showing the Jotle app icon"></div>
<h2 class="abs newsletter-title">SIGN UP FOR NEWSLETTER</h2>
<p class="abs newsletter-text">Duis sed odio sit amet nibh vulputate cursus a sit amet mauris. Morbi accumsan ipsum velit. Nam nec tellus a odio tincidunt auctor a ornare odio</p>
<div class="abs email-field"><svg width="16" height="12" viewBox="0 0 16 12"><rect x="0.5" y="0.5" width="15" height="11" fill="none" stroke="#aaa"/><polyline points="0.5,0.5 8,7 15.5,0.5" fill="none" stroke="#aaa"/></svg>Enter Your E-mail Adress</div>
<div class="abs signup-btn">SIGN-UP NOW</div>

<section class="disclaimer">
  <h2 class="abs disclaimer-title">DISCLAIMER</h2>
  <p class="abs disclaimer-text">Sed ut perspiciatis unde omnis iste natus error sit voluptatem accusantium doloremque laudantium, totam rem aperiam, eaque ipsa quae ab illo inventore veritatis et quasi architecto beatae vitae dicta sunt explicabo. Nemo enim ipsam voluptatem quia voluptas sit aspernatur aut odit aut fugit, sed quia consequuntur magni dolores eos</p>
</section>

<footer class="abs footer"></footer>
<div class="abs social" style="left:512px"></div>
<div class="abs social" style="left:550px"></div>
<div class="abs social" style="left:586px"></div>
<div class="abs social" style="left:622px"></div>
<div class="abs social" style="left:658px"></div>
<p class="abs footer-links">HOME &nbsp;/&nbsp; ABOUT US &nbsp;/&nbsp; FEATURES &nbsp;/&nbsp; REVIEWS &nbsp;/&nbsp; CONTACT US</p>
<p class="abs footer-copy">2017 © Copyrights Jotle.All Rights Reserved</p>

</body>
</html>
```